Research, Writing and Editing business needs a Business Card Design

I need a business card design for a new company based in Melbourne called The Bellwood Advisory Group. We provide research, writing and editing services. The company logo is attached, but I am open to your creative designs for business cards with the logo. As you will note, there are two potential logos. Feel free to use either of the logos.

The overall look I am hoping for is sleek, sophisticated, feminine and elegant.

Thanks in advance for your efforts.

Target Market(s)

Business professionals, academics and students

Industry/Entity Type

Business

Font styles to use
Serif
Script

Colors

Designer to choose colors to be used in the design.

Requirements
Must have
• The Bellwood Advisory Group
Dr Tessa Brennig

M: 0458 293 647
E: tessa@thebellwoodadvisorygroup.com.au
W: thebellwoodadvisorygroup.com.au
Nice to have
• Research | Writing | Editing

```html
<!DOCTYPE html>
<html lang="en">
<head>
<meta charset="utf-8">
<title>The Bellwood Advisory Group — Business Cards</title>
<link rel="stylesheet" href="https://fonts.googleapis.com/css2?family=Lato:wght@400;700&display=swap">
<style>
  :root {
    --backdrop: #e6e6e6;
    --card: #fbfbfa;
    --ink: #1a1a1a;
    --ink-soft: #2a2a2a;
    --card-shadow: rgba(0, 0, 0, 0.18);
  }
  * { box-sizing: border-box; margin: 0; padding: 0; }
  html, body {
    width: 1200px;
    height: 720px;
    overflow: hidden;
    background: var(--backdrop);
    font-family: "Lato", Arial, sans-serif;
    color: var(--ink);
  }
  .canvas {
    position: relative;
    width: 1200px;
    height: 720px;
  }
  .card {
    position: absolute;
    top: 242px;
    width: 420px;
    height: 238px;
    background: var(--card);
    box-shadow: 0 6px 18px var(--card-shadow);
  }
  .card--front { left: 147px; }
  .card--back { left: 633px; }

  .brand {
    font-family: "Lato", Arial, sans-serif;
    font-weight: 400;
    color: var(--ink);
    text-align: center;
    line-height: 1;
  }
  .brand__name { display: block; }
  .brand__sub { display: block; text-transform: uppercase; }

  .card--front .brand {
    position: absolute;
    top: 46px;
    right: 22px;
    width: 160px;
  }
  .card--front .brand__name { font-size: 21px; }
  .card--front .brand__sub { font-size: 7.5px; letter-spacing: 2.6px; margin-top: 5px; }

  .holder {
    position: absolute;
    left: 21px;
    top: 153px;
    font-weight: 700;
    font-size: 13px;
    color: var(--ink);
  }
  .contact-list {
    position: absolute;
    left: 21px;
    top: 184px;
    list-style: none;
  }
  .contact-list li {
    display: flex;
    align-items: center;
    height: 12px;
    font-size: 10px;
    color: var(--ink-soft);
  }
  .contact-list svg {
    width: 10px;
    height: 9px;
    margin-right: 6px;
    fill: var(--ink);
  }

  .card--back .brand {
    position: absolute;
    top: 102px;
    left: 0;
    width: 100%;
  }
  .card--back .brand__name { font-size: 30px; }
  .card--back .brand__sub { font-size: 10px; letter-spacing: 3.4px; margin-top: 6px; }

  .services {
    position: absolute;
    top: 174px;
    left: 0;
    width: 100%;
    text-align: center;
    font-size: 14px;
    color: var(--ink);
    letter-spacing: 0.3px;
  }
  .services .divider { margin: 0 5px; }
</style>
</head>
<body>
<main class="canvas">
  <section class="card card--front" aria-label="Business card front">
    <div class="brand">
      <span class="brand__name">The Bellwood</span>
      <span class="brand__sub">Advisory Group</span>
    </div>
    <h1 class="holder">Dr Tessa Brennig</h1>
    <ul class="contact-list">
      <li>
        <svg viewBox="0 0 10 9" aria-hidden="true"><path d="M0 3 C0 1 2 0 5 0 C8 0 10 1 10 3 L7.5 3.4 L7 2 L3 2 L2.5 3.4 Z M2 4 L8 4 L9 9 L1 9 Z"/></svg>
        0458 293 647
      </li>
      <li>
        <svg viewBox="0 0 10 9" aria-hidden="true"><path d="M0 1 L10 1 L10 8 L0 8 Z M1 2 L5 5 L9 2 Z" fill-rule="evenodd"/></svg>
        tessa@thebellwoodadvisorygroup.com.au
      </li>
      <li>
        <svg viewBox="0 0 10 9" aria-hidden="true"><path d="M0 0 L10 0 L10 7 L0 7 Z M1 1 L1 6 L9 6 L9 1 Z M3.5 8 L6.5 8 L6.5 9 L3.5 9 Z" fill-rule="evenodd"/></svg>
        thebellwoodadvisorygroup.com.au
      </li>
    </ul>
  </section>

  <section class="card card--back" aria-label="Business card back">
    <div class="brand">
      <span class="brand__name">The Bellwood</span>
      <span class="brand__sub">Advisory Group</span>
    </div>
    <p class="services">Research<span class="divider">|</span>Writing<span class="divider">|</span>Editing</p>
  </section>
</main>
</body>
</html>
```